Managed Service Provider email

We need an email designed that advertises our Managed Services product. We have been in business 28 years. Managed Services includes proactive ticketing, Help desk support, server and workstation monitoring, data backup monitoring, spam protection, regular reports, Deskflow 240, telecom services, ISP management, vendor management and more.

Target Market(s)

Business owners, decision makers, IT, CTO

Industry/Entity Type

Information Technology

Colors

Designer to choose colors to be used in the design.

Requirements
Must have
• Bullet points with included services. Mention of 28 years in business.
Nice to have
• We'd love our designer to read up on what an MSP (Managed Service Provider) does and use that information to find/create content for our email project.
Should not have
• A picture of a computer with a thermometer in its mouth.

```html
<!DOCTYPE html>
<html lang="en">
<head>
<meta charset="utf-8">
<title>Brevik Network Services – Managed IT</title>
<link href="https://fonts.googleapis.com/css2?family=Open+Sans:wdth,wght@75..100,300..800&display=swap" rel="stylesheet">
<style>
:root{
  --page:#ececec;
  --white:#ffffff;
  --blue:#1e8fe6;
  --blue-dark:#0f5fa8;
  --ink:#3a3f47;
  --text:#4a4f57;
  --muted:#8a8f96;
  --panel:#f5f6f8;
  --footer:#3b3f46;
}
*{margin:0;padding:0;box-sizing:border-box}
html,body{width:1200px;height:2826px;overflow:hidden}
body{background:var(--page);font-family:"Open Sans",Arial,sans-serif;color:var(--text)}
.email{position:absolute;left:198px;top:41px;width:812px;background:var(--white)}

.brand{display:flex;align-items:center;justify-content:center;gap:12px;font-weight:700;font-size:34px;color:var(--ink);letter-spacing:-.5px}
.brand-dot{width:22px;height:22px;border-radius:50%;background:var(--blue)}
.header{height:138px;display:flex;align-items:center;justify-content:center}

.hero{position:relative;height:501px;color:var(--white);text-align:center;overflow:hidden}
.hero-photo{position:absolute;inset:0;background:linear-gradient(120deg,#2a5d8e 0%,#3f7fb8 40%,#2d6aa3 70%,#1f4f80 100%)}
.hero-content{position:relative;padding-top:140px}
.hero-kicker{font-stretch:75%;font-weight:700;font-size:38px}
.hero-title{font-stretch:75%;font-weight:700;font-size:88px;line-height:1;margin-top:8px;letter-spacing:1px}
.hero-rule{width:700px;height:7px;background:var(--white);margin:12px auto 0}
.hero-sub{font-size:23px;line-height:36px;margin:26px auto 0;width:620px;font-weight:400}

.about{height:395px;text-align:center;padding-top:46px}
.section-title{color:var(--blue);font-size:40px;font-weight:400}
.about-copy{width:720px;margin:18px auto 0;font-size:17.5px;line-height:27px}
.about-copy strong{font-size:21px;font-weight:600;color:var(--ink)}
.btn{display:inline-block;background:var(--blue);color:var(--white);font-weight:700;font-size:20px;line-height:60px;padding:0 42px;text-decoration:none;border-radius:2px}
.about .btn{margin-top:38px;width:300px}

.band{position:relative;height:75px;background:var(--blue);color:var(--white);text-align:center;font-size:36px;line-height:75px}
.band::after{content:"";position:absolute;left:50%;bottom:-14px;margin-left:-14px;border-left:14px solid transparent;border-right:14px solid transparent;border-top:14px solid var(--blue)}

.services{position:relative;height:631px;background:var(--panel);padding:52px 0 0 40px;display:flex}
.svc-col{width:365px}
.svc-group{margin-bottom:20px}
.svc-head{font-size:25px;font-weight:600;color:var(--ink);margin-bottom:8px}
.svc-list{list-style:none;padding-left:16px}
.svc-list li{position:relative;padding-left:32px;font-size:17px;line-height:24px;margin-bottom:11px;color:var(--text)}
.svc-list li::before{content:"";position:absolute;left:0;top:2px;width:20px;height:20px;border-radius:50%;border:2px solid var(--blue);background:radial-gradient(circle,var(--blue) 0 4px,transparent 5px)}
.services .brand{position:absolute;right:56px;bottom:26px;font-size:30px}
.services .brand-dot{width:18px;height:18px}

.promo{position:relative;height:287px;background:var(--blue);color:var(--white);overflow:hidden}
.promo-photo{position:absolute;right:0;top:0;width:409px;height:100%;background:linear-gradient(90deg,rgba(30,143,230,0) 0%,#1f5e96 30%,#2b3f57 70%,#1e2a38 100%)}
.promo-text{position:relative;padding:36px 0 0 64px}
.promo-kicker{font-stretch:75%;font-weight:700;font-size:30px;color:#11365e}
.promo-years{font-weight:800;font-size:74px;line-height:1;letter-spacing:-1px}
.promo-biz{font-weight:300;font-size:46px;line-height:1.05}
.promo-note{font-stretch:75%;font-weight:700;font-size:30px;margin-top:4px}

.products{height:454px;text-align:center;padding-top:44px}
.partner-grid{display:flex;flex-wrap:wrap;justify-content:center;align-items:center;gap:24px 34px;width:760px;margin:40px auto 0}
.partner{font-size:30px;font-weight:600;color:#8c9096}
.products .btn{margin-top:56px;width:202px;padding:0}

.footer{height:273px;background:var(--footer);color:var(--white);text-align:center;padding-top:48px}
.footer .brand{color:var(--white)}
.address{font-size:18px;margin-top:42px}
.phone{display:flex;align-items:center;justify-content:center;gap:10px;font-size:31px;font-weight:700;margin-top:18px}
</style>
</head>
<body>
<main class="email">
  <header class="header">
    <div class="brand"><span class="brand-dot"></span>Brevik Network Services</div>
  </header>

  <section class="hero">
    <div class="hero-photo" role="img" aria-label="Technician working at server racks in a data centre, blue tinted"></div>
    <div class="hero-content">
      <p class="hero-kicker">Your Local, Friendly</p>
      <h1 class="hero-title">IT DEPARTMENT</h1>
      <div class="hero-rule"></div>
      <p class="hero-sub">We remotely manages your IT infrastructure and/or end-user systems</p>
    </div>
  </section>

  <section class="about">
    <h2 class="section-title">Why Brevik network services</h2>
    <p class="about-copy"><strong>With 28 years in business,</strong> Since we began installing business phone systems in 1990, Brevik Communications has a long history of providing telecommunications services to Southwest Missouri Businesses. Today, as Brevik Network Services we bring that long history of excellence to all of our services and products to a full suite of Information Technology Services.</p>
    <a class="btn" href="#">Read More About Us</a>
  </section>

  <h2 class="band">Our Services</h2>

  <section class="services">
    <div class="svc-col">
      <div class="svc-group">
        <h3 class="svc-head">Managed IT</h3>
        <ul class="svc-list"><li>Network Management</li><li>Workstation Monitoring</li><li>Server Monitoring</li></ul>
      </div>
      <div class="svc-group">
        <h3 class="svc-head">Business Phones</h3>
        <ul class="svc-list"><li>Systems</li><li>Mobile</li><li>SIP Trunking</li><li>Legacy</li></ul>
      </div>
      <div class="svc-group">
        <h3 class="svc-head">Cloud Services</h3>
        <ul class="svc-list"><li>Deskflow 240</li><li>Cloud Services</li><li>Cloud Application Implementation</li></ul>
      </div>
    </div>
    <div class="svc-col">
      <div class="svc-group">
        <h3 class="svc-head">Cabling</h3>
        <ul class="svc-list"><li>Structured Cabling</li><li>Fiber</li></ul>
      </div>
      <div class="svc-group">
        <h3 class="svc-head">Full Range of IT Services</h3>
        <ul class="svc-list">
          <li>Wireless Surveys, Design and Implementation</li>
          <li>Server Sales and Implementation - Delmar</li>
          <li>Workstation and Laptop Sales and Installation - Delmar</li>
          <li>Computer Hardware Upgrades</li>
          <li>Switching</li>
          <li>Network Engineering</li>
          <li>Firewalls and Web Filtering</li>
        </ul>
      </div>
    </div>
    <div class="brand"><span class="brand-dot"></span>Brevik</div>
  </section>

  <section class="promo">
    <div class="promo-photo" role="img" aria-label="Close view of networking equipment in a server rack"></div>
    <div class="promo-text">
      <p class="promo-kicker">Your Local Solution</p>
      <p class="promo-years">28 YEARS</p>
      <p class="promo-biz">In Business</p>
      <p class="promo-note">They Guarantee It</p>
    </div>
  </section>

  <section class="products">
    <h2 class="section-title">Our Products</h2>
    <div class="partner-grid">
      <span class="partner">Corvane</span>
      <span class="partner">Delmar</span>
      <span class="partner">Nimbusoft</span>
      <span class="partner">Deskflow 240</span>
      <span class="partner">Hartwell Enterprise</span>
      <span class="partner">Guardline</span>
      <span class="partner">Sistel</span>
      <span class="partner">Ubrix</span>
    </div>
    <a class="btn" href="#">View All</a>
  </section>

  <footer class="footer">
    <div class="brand"><span class="brand-dot"></span>Brevik Network Services</div>
    <p class="address">418 Harlow Avenue, Springfield, MO, 65810. United States</p>
    <p class="phone">
      <svg width="26" height="30" viewBox="0 0 24 24" aria-hidden="true"><path fill="#1e8fe6" d="M6.6 10.8a15.1 15.1 0 0 0 6.6 6.6l2.2-2.2c.3-.3.7-.4 1-.2 1.1.4 2.3.6 3.6.6.6 0 1 .4 1 1V20c0 .6-.4 1-1 1A17 17 0 0 1 3 4c0-.6.4-1 1-1h3.5c.6 0 1 .4 1 1 0 1.3.2 2.5.6 3.6.1.3 0 .7-.2 1z"/></svg>
      417 555 0182
    </p>
  </footer>
</main>
</body>
</html>
```